Medical Oncologist in Rural Australia needs a Business Card

I am a medical oncologist in a regional town in Australia. I need a business card that merges a degree of conservatism (as people's lives are entrusted to me) with cutting edge (as I am always trying to understand the latest cancer biology and trying to bring new drugs to patients rapidly). I wish my card to project the idea that I am trustworthy, caring and innovative. Not overly bold colours but something that doesn't drift into the background.

Medical

```html
<!DOCTYPE html>
<html lang="en">
<head>
<meta charset="utf-8">
<title>Riverbend Cancer Care – Business Card</title>
<link href="https://fonts.googleapis.com/css2?family=Open+Sans:wght@400;600&display=swap" rel="stylesheet">
<style>
  :root {
    --backdrop: #c4c4c4;
    --paper: #ffffff;
    --navy: #2a4196;
    --navy-deep: #233784;
    --navy-light: #3552b0;
    --sky: #6aaee0;
    --sky-soft: #9cc3ea;
    --ink-white: #ffffff;
  }
  * { box-sizing: border-box; margin: 0; padding: 0; }
  html, body {
    width: 1200px; height: 900px; overflow: hidden;
    background: var(--backdrop);
    font-family: "Open Sans", sans-serif;
  }
  .stage {
    position: relative; width: 1200px; height: 900px;
    display: flex; align-items: center; justify-content: center; gap: 50px;
  }
  .card {
    width: 525px; height: 300px; border-radius: 24px; overflow: hidden;
    position: relative;
    box-shadow: 0 10px 24px rgba(0,0,0,0.18);
  }
  /* Front */
  .card-front { background: var(--paper); }
  .front-brand {
    height: 158px; display: flex; align-items: center; gap: 14px;
    padding-left: 34px;
  }
  .brand-dot {
    width: 38px; height: 38px; border-radius: 50%; background: var(--navy);
    flex: none;
  }
  .brand-name {
    font-weight: 400; font-size: 33px; color: var(--navy); letter-spacing: 0.2px;
  }
  .front-stripe { height: 10px; background: var(--sky); }
  .front-details {
    position: absolute; left: 0; right: 0; top: 168px; bottom: 0;
    background: linear-gradient(180deg, var(--navy-light) 0%, var(--navy) 45%, var(--navy-deep) 100%);
    padding: 14px 30px;
    color: var(--ink-white);
  }
  .person-name { font-size: 17px; font-weight: 600; line-height: 1.2; }
  .person-credentials { font-size: 9.5px; color: var(--sky-soft); margin-bottom: 12px; }
  .contact-list { list-style: none; font-size: 13px; line-height: 1.35; }
  .contact-list li { display: flex; align-items: center; gap: 6px; }
  .contact-list svg { width: 11px; height: 11px; fill: var(--sky-soft); flex: none; }
  /* Back */
  .card-back {
    background: radial-gradient(ellipse at 40% 35%, var(--navy-light) 0%, var(--navy) 55%, var(--navy-deep) 100%);
    display: flex; align-items: center; justify-content: center; gap: 16px;
  }
  .card-back .brand-dot { background: var(--ink-white); width: 44px; height: 44px; }
  .card-back .brand-name { color: var(--ink-white); font-size: 36px; }
</style>
</head>
<body>
<main class="stage">
  <section class="card card-front" aria-label="Business card front">
    <div class="front-brand">
      <span class="brand-dot"></span>
      <span class="brand-name">Riverbend Cancer Care</span>
    </div>
    <div class="front-stripe"></div>
    <div class="front-details">
      <p class="person-name">Alan Mercer</p>
      <p class="person-credentials">MBBS (hons), FRACP, BE (hons)</p>
      <ul class="contact-list">
        <li><svg viewBox="0 0 24 24"><path d="M6.6 10.8a15 15 0 0 0 6.6 6.6l2.2-2.2c.3-.3.7-.4 1-.2 1.1.4 2.3.6 3.6.6.6 0 1 .4 1 1V20c0 .6-.4 1-1 1A17 17 0 0 1 3 4c0-.6.4-1 1-1h3.5c.6 0 1 .4 1 1 0 1.3.2 2.5.6 3.6.1.3 0 .7-.2 1z"/></svg>555-210-4837</li>
        <li><svg viewBox="0 0 24 24"><path d="M12 2a10 10 0 1 0 0 20 10 10 0 0 0 0-20zm6.9 6h-3a15 15 0 0 0-1.3-3.9A8 8 0 0 1 18.9 8zM12 4c.8 1.2 1.5 2.5 1.9 4h-3.8c.4-1.5 1.1-2.8 1.9-4zM4.3 14a8 8 0 0 1 0-4h3.4a16 16 0 0 0 0 4zm.8 2h3a15 15 0 0 0 1.3 3.9A8 8 0 0 1 5.1 16zm3-8h-3a8 8 0 0 1 4.3-3.9A15 15 0 0 0 8.1 8zM12 20c-.8-1.2-1.5-2.5-1.9-4h3.8c-.4 1.5-1.1 2.8-1.9 4zm2.3-6H9.7a14 14 0 0 1 0-4h4.6a14 14 0 0 1 0 4zm.3 5.9a15 15 0 0 0 1.3-3.9h3a8 8 0 0 1-4.3 3.9zm1.7-5.9a16 16 0 0 0 0-4h3.4a8 8 0 0 1 0 4z"/></svg>www.riverbendcare.com</li>
        <li><svg viewBox="0 0 24 24"><path d="M2 5h20v14H2zm2 2v.5l8 5 8-5V7zm0 2.8V17h16V9.8l-8 5z"/></svg>info@riverbendcare.com</li>
        <li><svg viewBox="0 0 24 24"><path d="M12 3 2 12h3v8h5v-5h4v5h5v-8h3z"/></svg>48 Harbour Lane Millbrook</li>
      </ul>
    </div>
  </section>

  <section class="card card-back" aria-label="Business card back">
    <span class="brand-dot"></span>
    <span class="brand-name">Riverbend Cancer Care</span>
  </section>
</main>
</body>
</html>
```